Brook Vantage claims recovery services

Its a new company in Dubai UAE. The company activity is debt management, debt collection, loans settlements and restructuring. The company involved in any business or sector requires debt management including government entities, Medical & Health care sector, Banks & finance companies, SME's and commercial business.

Target Market(s)

government entities, Medical & Health care sector, Banks & finance companies, SME's and commercial business.

Industry/Entity Type

Financial Service

Number of Pages Required

5+ page

Requirements
Must have
• Focus on the services not the team and clients
Should not have
• Colorful . Shouldn't have Client testimonial and our clients

```html
<!DOCTYPE html>
<html lang="en">
<head>
<meta charset="utf-8">
<title>Brook Vantage – Claims Recovery Services</title>
<link href="https://fonts.googleapis.com/css2?family=Cinzel:wght@400;600&family=Lato:wght@400;700&display=swap" rel="stylesheet">
<style>
:root{
  --navy:#25476d;
  --navy-dark:#1d3a5a;
  --ink:#1d1d1d;
  --grey-bg:#f2f2f2;
  --nav-top:#9a9a9a;
  --nav-bottom:#7a7a7a;
  --black:#000;
  --white:#fff;
  --muted:#555;
  --footer:#151515;
}
*{margin:0;padding:0;box-sizing:border-box}
html,body{width:669px;height:1200px;overflow:hidden;background:var(--white)}
body{position:relative;font-family:'Lato',sans-serif;color:var(--ink)}
.abs{position:absolute}

/* header */
.header{left:0;top:0;width:669px;height:52px;background:var(--white)}
.brand{left:55px;top:14px;display:flex;align-items:center;gap:6px}
.brand-mark{width:22px;height:22px;background:var(--navy)}
.brand-name{font-family:'Cinzel',serif;font-size:15px;color:var(--navy);letter-spacing:.5px}
.contact{top:18px;display:flex;align-items:center;gap:8px;font-size:8px;color:#333}
.contact svg{width:16px;height:16px}

/* nav */
.nav{left:0;top:52px;width:669px;height:27px;background:linear-gradient(var(--nav-top),var(--nav-bottom));display:flex;padding-left:55px}
.nav a{font-family:'Cinzel',serif;font-size:8px;color:var(--white);text-decoration:none;display:flex;align-items:center;justify-content:center;border-right:1px solid rgba(255,255,255,.25);height:27px}
.nav a.active{background:var(--navy)}

/* hero */
.hero{left:0;top:79px;width:669px;height:286px;background:linear-gradient(100deg,#1f4468 0%,#2c5a85 45%,#c9c2b6 75%,#e6e2db 100%)}
.hero-title{left:51px;top:150px;font-family:'Cinzel',serif;font-weight:400;font-size:16px;line-height:24px;color:var(--white);letter-spacing:.5px}
.dots{left:311px;top:341px;display:flex;gap:5px}
.dots span{width:7px;height:7px;border-radius:50%;background:#333}
.dots span.on{background:var(--navy);box-shadow:0 0 0 1px #fff}

/* section heading */
.heading{width:669px;text-align:center;font-family:'Cinzel',serif;font-weight:400;font-size:18px;color:var(--ink)}
.heading em{font-style:normal;color:var(--navy)}
.rule{left:0;width:669px;height:10px}

/* welcome */
.welcome{left:0;top:365px;width:669px;height:203px;background:var(--grey-bg)}
.intro{left:62px;top:434px;width:545px;text-align:center;font-size:6.8px;line-height:12.5px}
.feature{top:485px;width:180px;display:flex;gap:12px}
.feature-icon{width:52px;height:52px;border-radius:50%;background:var(--navy);border:3px solid var(--white);box-shadow:0 1px 4px rgba(0,0,0,.35);flex:none;display:flex;align-items:center;justify-content:center}
.feature h3{font-family:'Cinzel',serif;font-weight:400;font-size:11px;margin:2px 0 4px}
.feature p{font-size:6.8px;line-height:12.3px}
.divider{top:490px;width:1px;height:48px;background:#d8d8d8}

/* services */
.services{left:0;top:568px;width:669px;height:308px;background:var(--black)}
.card{top:636px;width:107px;height:209px;background:var(--white);border-bottom:3px solid var(--navy)}
.card-photo{height:92px;background:linear-gradient(150deg,#7f94aa,#d7dde4)}
.card-badge{position:absolute;left:44px;top:83px;width:19px;height:19px;border-radius:50%;background:var(--white);display:flex;align-items:center;justify-content:center}
.card-badge span{width:7px;height:7px;background:var(--navy)}
.card h4{font-family:'Cinzel',serif;font-weight:400;font-size:10px;line-height:10.5px;text-align:center;margin:12px 0 6px;height:21px;display:flex;align-items:center;justify-content:center;color:var(--ink)}
.card p{font-size:6.6px;line-height:10.5px;text-align:center;padding:0 5px}
.card-plus{position:absolute;left:45px;bottom:-3px;width:17px;height:10px;background:var(--navy);border-radius:9px 9px 0 0;color:#fff;font-size:10px;line-height:10px;text-align:center;font-weight:700}

/* covering */
.covering{left:0;top:876px;width:669px;height:269px;background:#f4f4f4}
.sector{width:36px;height:36px;border-radius:50%;background:var(--white);box-shadow:0 1px 4px rgba(0,0,0,.3);display:flex;align-items:center;justify-content:center}
.sector svg{width:18px;height:18px}
.sector-label{font-family:'Cinzel',serif;font-size:8px;color:#333;line-height:10px}

/* footer */
.footer{left:0;top:1145px;width:669px;height:32px;background:var(--footer);display:flex;align-items:center;padding-left:55px;gap:14px;color:#ddd;font-size:8.5px}
.footer .item{display:flex;align-items:center;gap:6px}
.social{position:absolute;right:55px;top:9px;display:flex;gap:4px}
.social span{width:15px;height:15px;border-radius:50%;background:var(--white)}
.copyright{left:0;top:1177px;width:669px;height:23px;background:var(--navy);color:var(--white);font-size:7.5px;text-align:center;line-height:23px}
</style>
</head>
<body>

<header class="abs header">
  <div class="abs brand"><span class="brand-mark"></span><span class="brand-name">Brook Vantage</span></div>
  <div class="abs contact" style="left:404px">
    <svg viewBox="0 0 16 16"><path d="M8 1 L15 8 L8 15 L1 8Z" fill="none" stroke="#25476d" stroke-width="1.6"/><path d="M6 6c0 2 2 4 4 4" stroke="#25476d" stroke-width="1.4" fill="none"/></svg>
    123-456-7890
  </div>
  <div class="abs contact" style="left:510px">
    <svg viewBox="0 0 16 16"><path d="M8 1 L15 8 L8 15 L1 8Z" fill="none" stroke="#25476d" stroke-width="1.6"/><rect x="5" y="6" width="6" height="4" fill="#25476d"/></svg>
    info@brookvantage.com
  </div>
</header>

<nav class="abs nav">
  <a class="active" style="width:53px">Home</a>
  <a style="width:110px">About Us</a>
  <a style="width:136px">Our Services</a>
  <a style="width:120px">Team</a>
  <a style="width:140px;border-right:none">Contact Us</a>
</nav>

<div class="abs hero" role="img" aria-label="Businessman's hand stopping a row of falling wooden dominoes"></div>
<h1 class="abs hero-title">Managing your money<br>recovering your<br>relationships</h1>
<div class="abs dots"><span class="on"></span><span></span><span></span><span></span></div>

<section class="abs welcome"></section>
<h2 class="abs heading" style="top:387px">Welcome to <em>Brook Vantage.</em></h2>
<svg class="abs rule" style="top:410px" viewBox="0 0 669 10"><line x1="207" y1="5" x2="462" y2="5" stroke="#25476d" stroke-width=".8"/><rect x="331" y="2" width="6" height="6" transform="rotate(45 334 5)" fill="#f2f2f2" stroke="#25476d"/></svg>
<p class="abs intro">We are a Claims Recovery and Debt Management Services company based in Dubai, United Arab Emirates. The Brook Vantage team handles a comprehensive range of debt recoveries, such as invoices; insurance payments; supplier and rent payments; and personal and business loans, for individuals and businesses across an array of industries. Brook Vantage was founded on traditional values, and we're proud of our personal approach.</p>

<div class="abs feature" style="left:60px">
  <div class="feature-icon"><svg width="28" height="28" viewBox="0 0 28 28" fill="none" stroke="#fff" stroke-width="2.2"><circle cx="13" cy="15" r="10"/><circle cx="13" cy="15" r="5.5"/><circle cx="13" cy="15" r="1.5" fill="#fff"/><path d="M13 15 L24 4 M20 4h4v4"/></svg></div>
  <div><h3>Mission</h3><p>Brook Vantage is a leading Debt Management and Claims Recovery Services..... [ + ]</p></div>
</div>
<div class="abs divider" style="left:242px"></div>
<div class="abs feature" style="left:256px">
  <div class="feature-icon"><svg width="30" height="30" viewBox="0 0 30 30"><path d="M2 15 Q15 3 28 15 Q15 27 2 15Z" fill="#fff"/><circle cx="15" cy="15" r="5.5" fill="#25476d"/><circle cx="15" cy="15" r="2.5" fill="#fff"/></svg></div>
  <div><h3>Vision</h3><p>Our success is built on traditions of trust, valued and respect .....[+]</p></div>
</div>
<div class="abs divider" style="left:437px"></div>
<div class="abs feature" style="left:452px">
  <div class="feature-icon"><svg width="30" height="30" viewBox="0 0 30 30" fill="none" stroke="#fff" stroke-width="2" stroke-linejoin="round"><path d="M2 11 L8 8 L14 11 L20 8 L28 11 M6 17 L12 22 Q14 23 16 21 L22 16 M9 14 L15 19 M12 12 L18 17"/></svg></div>
  <div><h3>Values</h3><p>At Brook Vantage, our values are born of time-honoured traditions... [ + ]</p></div>
</div>

<section class="abs services"></section>
<h2 class="abs heading" style="top:590px;color:var(--white)">Our Services</h2>
<svg class="abs rule" style="top:613px" viewBox="0 0 669 10"><line x1="240" y1="5" x2="430" y2="5" stroke="#888" stroke-width=".8"/><rect x="331" y="2" width="6" height="6" transform="rotate(45 334 5)" fill="#000" stroke="#bbb"/></svg>

<article class="abs card" style="left:55px">
  <div class="card-photo" role="img" aria-label="Business people reviewing charts on a tablet"></div>
  <div class="card-badge"><span></span></div>
  <h4>Recovery<br>Solutions</h4>
  <p>Our experience has taught us that when it comes to recovery, it always pays to find the most amicable solution,</p>
  <div class="card-plus">+</div>
</article>
<article class="abs card" style="left:168px">
  <div class="card-photo" role="img" aria-label="Calculator, pen and financial bar charts"></div>
  <div class="card-badge"><span></span></div>
  <h4>Debt<br>Management</h4>
  <p>At Brook Vantage, we pull together our wisdom and expertise to make debt work for you.</p>
  <div class="card-plus">+</div>
</article>
<article class="abs card" style="left:281px">
  <div class="card-photo" style="background:linear-gradient(150deg,#f3f3f3,#d9d9d9)" role="img" aria-label="Magnifying glass over the words debt settlement"></div>
  <div class="card-badge"><span></span></div>
  <h4>Debt<br>Settlement</h4>
  <p>Lorem ipsum dolor sit amet, consectetuer adipiscing elit, sed diam nonummy nibh euismod tincidunt ut laoreet dolore</p>
  <div class="card-plus">+</div>
</article>
<article class="abs card" style="left:394px">
  <div class="card-photo" role="img" aria-label="Business partners shaking hands outside an office"></div>
  <div class="card-badge"><span></span></div>
  <h4>Outsourcing</h4>
  <p>Lorem ipsum dolor sit amet, consectetuer adipiscing elit, sed diam nonummy nibh euismod tincidunt ut laoreet dolore</p>
  <div class="card-plus">+</div>
</article>
<article class="abs card" style="left:507px">
  <div class="card-photo" style="background:linear-gradient(150deg,#cfe0ec,#6e93b3)" role="img" aria-label="Hands typing on a laptop keyboard"></div>
  <div class="card-badge"><span></span></div>
  <h4>Interactive<br>Online Access</h4>
  <p>Lorem ipsum dolor sit amet, consectetuer adipiscing elit, sed diam nonummy nibh euismod tincidunt ut laoreet dolore</p>
  <div class="card-plus">+</div>
</article>

<section class="abs covering"></section>
<h2 class="abs heading" style="top:898px">We are <em>Covering</em></h2>
<svg class="abs rule" style="top:921px" viewBox="0 0 669 10"><line x1="230" y1="5" x2="444" y2="5" stroke="#25476d" stroke-width=".8"/><rect x="331" y="2" width="6" height="6" transform="rotate(45 334 5)" fill="#f4f4f4" stroke="#25476d"/></svg>

<svg class="abs" style="left:0;top:960px" width="669" height="185" viewBox="0 0 669 185">
  <path d="M212 185 A122 122 0 0 1 456 185" fill="none" stroke="#d6d6d6" stroke-width="14"/>
  <path d="M226 185 A108 108 0 0 1 442 185" fill="#fff"/>
  <g stroke="#9fb3c6" stroke-width="1">
    <line x1="216" y1="143" x2="193" y2="131"/>
    <line x1="250" y1="97" x2="230" y2="78"/>
    <line x1="296" y1="74" x2="292" y2="44"/>
    <line x1="358" y1="74" x2="362" y2="44"/>
    <line x1="403" y1="96" x2="423" y2="78"/>
    <line x1="437" y1="142" x2="460" y2="131"/>
  </g>
  <g fill="#5d88b0">
    <circle cx="216" cy="143" r="2.5"/><circle cx="250" cy="97" r="2.5"/><circle cx="296" cy="74" r="2.5"/>
    <circle cx="358" cy="74" r="2.5"/><circle cx="403" cy="96" r="2.5"/><circle cx="437" cy="142" r="2.5"/>
  </g>
</svg>

<div class="abs sector" style="left:269px;top:970px"><svg viewBox="0 0 18 18" fill="#111"><path d="M2 3h14l1 4H1z"/><rect x="2" y="8" width="14" height="8"/><rect x="5" y="10" width="4" height="6" fill="#fff"/></svg></div>
<div class="abs sector-label" style="left:241px;top:982px">SME</div>
<div class="abs sector" style="left:348px;top:970px"><svg viewBox="0 0 18 18"><rect x="1" y="5" width="16" height="11" rx="2" fill="#111"/><rect x="6" y="2" width="6" height="4" fill="none" stroke="#111" stroke-width="1.5"/><path d="M9 8v6M6 11h6" stroke="#fff" stroke-width="2"/></svg></div>
<div class="abs sector-label" style="left:394px;top:984px">Health Care</div>
<div class="abs sector" style="left:199px;top:1005px"><svg viewBox="0 0 18 18" fill="#111"><path d="M9 1 L17 5H1z"/><rect x="2" y="6" width="14" height="2"/><rect x="3" y="9" width="2" height="5"/><rect x="8" y="9" width="2" height="5"/><rect x="13" y="9" width="2" height="5"/><rect x="1" y="15" width="16" height="2"/></svg></div>
<div class="abs sector-label" style="left:162px;top:1015px">Banks</div>
<div class="abs sector" style="left:419px;top:1005px"><svg viewBox="0 0 18 18" fill="#111"><rect x="4" y="2" width="10" height="15"/><g fill="#fff"><rect x="6" y="4" width="2" height="2"/><rect x="10" y="4" width="2" height="2"/><rect x="6" y="8" width="2" height="2"/><rect x="10" y="8" width="2" height="2"/><rect x="8" y="13" width="2" height="4"/></g></svg></div>
<div class="abs sector-label" style="left:467px;top:1017px">Commercial</div>
<div class="abs sector" style="left:157px;top:1073px"><svg viewBox="0 0 18 18" fill="#111"><path d="M9 1 L17 5H1z"/><rect x="2" y="6" width="14" height="2"/><rect x="3" y="9" width="2" height="5"/><rect x="8" y="9" width="2" height="5"/><rect x="13" y="9" width="2" height="5"/><rect x="1" y="15" width="16" height="2"/></svg></div>
<div class="abs sector-label" style="left:86px;top:1081px;text-align:center">Government<br>Entities</div>
<div class="abs sector" style="left:461px;top:1073px"><svg viewBox="0 0 18 18" fill="#111"><path d="M1 17V6l5 3V6l5 3V6l5 3V2h1v15z"/><g fill="#fff"><rect x="4" y="12" width="2" height="2"/><rect x="8" y="12" width="2" height="2"/><rect x="12" y="12" width="2" height="2"/></g></svg></div>
<div class="abs sector-label" style="left:504px;top:1085px">Industrial</div>

<footer class="abs footer">
  <span class="item"><svg width="10" height="13" viewBox="0 0 10 13"><path d="M5 0a5 5 0 0 1 5 5c0 3-5 8-5 8S0 8 0 5a5 5 0 0 1 5-5z" fill="#ddd"/><circle cx="5" cy="5" r="1.8" fill="#151515"/></svg>Lorem ipsum dolor sit amet, adipiscing elit</span>
  <span class="item"><svg width="10" height="11" viewBox="0 0 10 11"><path d="M2 0l2 3-1 1.5c.8 1.5 2 2.7 3.5 3.5L8 7l2 2-1.5 2C4 10 0 6 0 1.5z" fill="#ddd"/></svg>123-456-7890</span>
  <span class="item"><svg width="12" height="9" viewBox="0 0 12 9"><rect width="12" height="9" fill="#ddd"/><path d="M0 0l6 5 6-5" stroke="#151515" fill="none"/></svg>info@brookvantage.com</span>
  <div class="social"><span></span><span></span><span></span><span></span></div>
</footer>
<div class="abs copyright">Copyright 2016 Brookvantage. All rights reserved.</div>

</body>
</html>
```